New Architectural Firm Business Cards

New Business card to compliment previous pixel forum logo (attached). Please design a business card that is simple, modern, creative....please do not use "symbols", simply the logo and associated graphics/text. The front should contain name/address/phone/email/web address (with graphics).....back should be 100% graphic design using the logo somehow. Hoping for a two color (black and yellow) design. full bleed design, no borders

Target Market(s)

Commercial Architecture Clients

Industry/Entity Type

Architecture

Contact Information for Business Card

Please design a business card that is simple, modern, creative....please do not use "symbols", simply the logo and associated graphics/text. The front should contain name/address/phone/email/web address (with graphics).....back should be 100% graphic design using the logo somehow

Font styles to use
Sans Serif

Colors
FFF300
FFF600
FEFA6F
FFFEC7
FFFEE8

Requirements
Must have
• Clean, Modern Design
Should not have
• Stock images or "icons"

```html
<!DOCTYPE html>
<html lang="en">
<head>
<meta charset="utf-8">
<title>pixel forum – business cards</title>
<link rel="stylesheet" href="https://fonts.googleapis.com/css2?family=Urbanist:wght@400;500;700;800&display=swap">
<style>
  :root {
    --backdrop: #1f1f1f;
    --card-light: #e9e9ea;
    --card-dark: #191919;
    --brand-yellow: #e4b816;
    --ink: #1c1c1c;
    --mark-grey: #8c8c8c;
  }
  * { margin: 0; padding: 0; box-sizing: border-box; }
  html, body {
    width: 1200px; height: 1200px; overflow: hidden;
    background: var(--backdrop);
    font-family: "Urbanist", sans-serif;
  }
  .canvas { position: relative; width: 1200px; height: 1200px; }

  .card {
    position: absolute; left: 227px; width: 746px; height: 425px;
  }
  .card--front { top: 135px; background: var(--card-light); }
  .card--back  { top: 640px; background: var(--card-dark); }

  .brand-name {
    position: absolute;
    font-weight: 800;
    letter-spacing: -1px;
    line-height: 1;
    white-space: nowrap;
  }
  .card--front .brand-name {
    left: 48px; top: 165px;
    font-size: 46px;
    color: var(--brand-yellow);
  }
  .card--back .brand-name {
    left: 0; right: 0; top: 180px;
    text-align: center;
    font-size: 64px;
    color: var(--mark-grey);
  }

  .divider {
    position: absolute; left: 341px; top: 97px;
    width: 2px; height: 235px; background: var(--ink);
  }

  .details { position: absolute; left: 387px; top: 92px; color: var(--ink); }
  .details__name {
    font-size: 26px; font-weight: 800; color: var(--brand-yellow);
    letter-spacing: 0.2px; line-height: 1.1;
  }
  .details__role { font-size: 19px; font-weight: 500; margin-top: 2px; }
  .details__address { font-size: 19px; font-weight: 500; line-height: 25px; margin-top: 36px; }
  .details__contact { list-style: none; font-size: 19px; font-weight: 500; line-height: 25.5px; margin-top: 31px; }
  .details__label { color: var(--brand-yellow); margin-right: 5px; }
</style>
</head>
<body>
<main class="canvas">
  <section class="card card--front" aria-label="Business card front">
    <div class="brand-name">pixel forum</div>
    <div class="divider"></div>
    <div class="details">
      <h1 class="details__name">MARCUS HALE</h1>
      <p class="details__role">Principal Architect</p>
      <p class="details__address">Unit 12 Harbour Yard<br>8 Calder Lane, London, N4 2QT</p>
      <ul class="details__contact">
        <li><span class="details__label">p.</span>+44 (0) 20 7946 0321</li>
        <li><span class="details__label">e.</span>studio@pixelforum.com</li>
        <li><span class="details__label">w.</span>www.pixelforum.com</li>
      </ul>
    </div>
  </section>

  <section class="card card--back" aria-label="Business card back">
    <div class="brand-name">pixel forum</div>
  </section>
</main>
</body>
</html>
```